Maple Ridge business card design

Card needs to include the following text/items:
Company Logo
Tobin Marsh
Phone # - 555-318-7642
service@mapleridgelandscaping.example
Lawn & landscape maintenance services

```html
<!DOCTYPE html>
<html lang="en">
<head>
<meta charset="utf-8">
<title>Maple Ridge Landscaping – Business Card</title>
<link rel="stylesheet" href="https://fonts.googleapis.com/css2?family=Open+Sans:wght@400;600&display=swap">
<style>
  :root {
    --forest: #0b4023;
    --olive: #869a2e;
    --paper: #ffffff;
    --stage: #e6e6e6;
    --sky: #e9eef1;
    --mist: #dde3df;
  }
  * { margin: 0; padding: 0; box-sizing: border-box; }
  html, body { width: 1200px; height: 1200px; overflow: hidden; }
  body {
    background: radial-gradient(circle at 50% 50%, #f6f6f6 0%, var(--stage) 75%);
    font-family: "Open Sans", sans-serif;
    position: relative;
  }
  .card {
    position: absolute;
    left: 254px;
    width: 692px;
    height: 385px;
    border: 1.5px solid var(--forest);
    border-radius: 28px;
    overflow: hidden;
    background: var(--paper);
  }
  .card--front { top: 157px; }
  .card--back { top: 658px; }
  .card__band {
    position: absolute;
    left: 0; right: 0; bottom: 0;
    height: 13px;
    display: flex;
  }
  .card__band-olive { flex: 0 0 325px; background: var(--olive); }
  .card__band-forest { flex: 1; background: var(--forest); }
  .notch {
    position: absolute;
    top: 159px;
    width: 80px; height: 80px;
    border: 2px solid var(--olive);
    border-radius: 50%;
  }
  .notch--left { left: -41px; }
  .notch--right { right: -41px; }

  .brand { position: absolute; text-align: center; color: var(--forest); font-weight: 600; }
  .brand__mark { display: block; margin: 0 auto; border-radius: 50%; }
  .brand__name { display: block; line-height: 1; }
  .brand__sub { display: block; line-height: 1; }

  .card--front .brand { left: 70px; top: 107px; width: 190px; }
  .card--front .brand__mark { width: 130px; height: 130px; }
  .card--front .brand__name { font-size: 27px; margin-top: 6px; }
  .card--front .brand__sub { font-size: 11px; letter-spacing: 8px; margin-top: 4px; padding-left: 8px; }

  .divider {
    position: absolute;
    left: 281px; top: 124px;
    width: 2px; height: 147px;
    background: var(--olive);
    border-radius: 1px;
  }
  .contact { position: absolute; left: 313px; top: 121px; color: var(--forest); }
  .contact__name { font-size: 22px; font-weight: 400; line-height: 1.2; }
  .contact__role { font-size: 14px; color: var(--olive); margin-top: 1px; }
  .contact__list { list-style: none; margin-top: 30px; }
  .contact__item { display: flex; align-items: center; gap: 4px; font-size: 16px; height: 28px; }
  .contact__icon { width: 20px; height: 20px; flex: none; }

  .card__scene {
    position: absolute; inset: 0;
    background: linear-gradient(100deg, var(--sky) 0%, #eee9e4 40%, var(--mist) 70%, #d6ddd8 100%);
  }
  .card--back .brand { left: 0; right: 0; top: 76px; }
  .card--back .brand__mark { width: 214px; height: 214px; }
  .card--back .brand__name { font-size: 46px; margin-top: 8px; }
  .card--back .brand__sub { font-size: 19px; letter-spacing: 15px; margin-top: 6px; padding-left: 15px; }
</style>
</head>
<body>
  <section class="card card--front">
    <div class="notch notch--left"></div>
    <div class="notch notch--right"></div>
    <div class="brand">
      <span class="brand__mark" style="background: radial-gradient(circle at 50% 35%, #5fb6d8, #2f6b3a 70%, var(--forest));" role="img" aria-label="Logo emblem area: landscape scene with trees and hills"></span>
      <span class="brand__name">Maple Ridge</span>
      <span class="brand__sub">LANDSCAPING</span>
    </div>
    <div class="divider"></div>
    <div class="contact">
      <h1 class="contact__name">Tobin Marsh</h1>
      <p class="contact__role">Lawn &amp; Landscape Maintenance Services</p>
      <ul class="contact__list">
        <li class="contact__item">
          <svg class="contact__icon" viewBox="0 0 20 20" aria-hidden="true"><circle cx="10" cy="10" r="10" fill="#869a2e"/><path d="M7 5.2l1.6-.4 1 2.6-1.1.9c.5 1.4 1.3 2.4 2.3 3.2l1.1-.8 2.3 1.5-.5 1.6c-.3.6-1 .8-1.7.6-3-1-5-3.6-5.7-6.9-.1-.9.2-1.9.7-2.3z" fill="#fff"/></svg>
          <span>555-318-7642</span>
        </li>
        <li class="contact__item">
          <svg class="contact__icon" viewBox="0 0 20 20" aria-hidden="true"><circle cx="10" cy="10" r="10" fill="#869a2e"/><rect x="5" y="6.5" width="10" height="7" rx="0.8" fill="#fff"/><path d="M5.3 7l4.7 3.6L14.7 7" fill="none" stroke="#869a2e" stroke-width="0.9"/></svg>
          <span>service@mapleridgelandscaping.example</span>
        </li>
      </ul>
    </div>
    <div class="card__band"><span class="card__band-olive"></span><span class="card__band-forest"></span></div>
  </section>

  <section class="card card--back">
    <div class="card__scene" role="img" aria-label="Faded background illustration of bare tree, sun, hills and evergreen"></div>
    <div class="brand">
      <span class="brand__mark" style="background: radial-gradient(circle at 50% 35%, #5fb6d8, #2f6b3a 70%, var(--forest));" role="img" aria-label="Logo emblem area: landscape scene with trees and hills"></span>
      <span class="brand__name">Maple Ridge</span>
      <span class="brand__sub">LANDSCAPING</span>
    </div>
    <div class="card__band"><span class="card__band-olive"></span><span class="card__band-forest"></span></div>
  </section>
</body>
</html>
```